Fun, Clean Business Card For Family Focused Travel Agency

I need a business card using specific colors and fonts as in the uploaded files. Ideally, I would like a large image of the logo on the back and all the contact info on the front. Maybe the stars/dots somewhere in a flowy form.

I do want it the contact information to be clear and easy to read. I don't want it to look too busy. Maybe even a bit minimalist.

I plan or ordering the ROUNDED CORNER business cards from Cardwell Press, so please consider that in your design.

Target Market(s)

Families with children, couples, groups of friends

Contact Information for Business Card

Marla Quent, Owner
Marla@TidewayTrips.example
Cell Phone Number 555-218-6034
Office Phone Number 555-647-1295
Specializing in Fablecrest destinations, Goldmere Parkside Resort, Cruises and All-Inclusive Vacations.

Nice but not required:
www.TidewayTrips.example
Facebook, Instagram, Twitter icons with username: TidewayTrips

Font styles to use
Sans Serif

Requirements
Must have
• Please try to use the colors from the logo as much as possible. I understand lighter shades/colors may be needed for some things.
Should not have
• NO SERIF FONTS. That is really the only thing I do not want at all

```html
<!DOCTYPE html>
<html lang="en">
<head>
<meta charset="utf-8">
<title>Tideway Trips — Business Card</title>
<link href="https://fonts.googleapis.com/css2?family=Ubuntu:wght@400;500;700&display=swap" rel="stylesheet">
<style>
  :root {
    --backdrop: #cfe9e1;
    --teal: #1fb79b;
    --navy: #19224f;
    --white: #ffffff;
    --card-shadow: rgba(20, 70, 60, 0.18);
  }
  * { box-sizing: border-box; margin: 0; padding: 0; }
  html, body {
    width: 1200px;
    height: 856px;
    overflow: hidden;
  }
  body {
    background: var(--backdrop);
    font-family: "Ubuntu", sans-serif;
    display: flex;
    align-items: center;
    justify-content: center;
    gap: 48px;
  }
  .card {
    position: relative;
    width: 540px;
    height: 308px;
    border-radius: 26px;
    box-shadow: 0 10px 28px var(--card-shadow);
  }
  .card--front { background: var(--teal); color: var(--white); }
  .card--back { background: var(--white); color: var(--navy); }

  .brand {
    display: flex;
    align-items: center;
    gap: 10px;
    font-weight: 500;
    white-space: nowrap;
  }
  .brand__dot {
    border-radius: 50%;
    flex: none;
  }
  .card--front .brand {
    position: absolute;
    left: 42px;
    top: 108px;
    font-size: 30px;
    color: var(--white);
  }
  .card--front .brand__dot {
    width: 30px; height: 30px;
    background: var(--white);
  }

  .contact {
    position: absolute;
    left: 298px;
    top: 48px;
  }
  .contact__name {
    font-size: 21px;
    font-weight: 700;
    color: var(--navy);
    letter-spacing: 0.5px;
    margin-bottom: 10px;
  }
  .contact__line {
    font-size: 13.5px;
    line-height: 1.4;
    color: var(--white);
  }

  .specialties {
    position: absolute;
    left: 40px;
    right: 40px;
    top: 206px;
    text-align: center;
    font-size: 15px;
    font-weight: 500;
    line-height: 1.45;
  }

  .card--back .brand {
    position: absolute;
    left: 0; right: 0;
    top: 104px;
    justify-content: center;
    font-size: 46px;
    color: var(--navy);
  }
  .card--back .brand__dot {
    width: 44px; height: 44px;
    background: var(--teal);
  }
  .website {
    position: absolute;
    left: 0; right: 0;
    top: 196px;
    text-align: center;
    font-size: 15px;
    font-weight: 700;
    color: var(--navy);
  }
</style>
</head>
<body>
  <section class="card card--front" aria-label="Card front">
    <div class="brand">
      <span class="brand__dot"></span>
      <span class="brand__name">Tideway Trips</span>
    </div>
    <div class="contact">
      <p class="contact__name">MARLA QUENT</p>
      <p class="contact__line">Marla@TidewayTrips.example</p>
      <p class="contact__line">555-218-6034</p>
      <p class="contact__line">555-647-1295</p>
    </div>
    <p class="specialties">Specializing in Fablecrest destinations, Goldmere Parkside Resort,<br>Cruises and All-Inclusive Vacations.</p>
  </section>

  <section class="card card--back" aria-label="Card back">
    <div class="brand">
      <span class="brand__dot"></span>
      <span class="brand__name">Tideway Trips</span>
    </div>
    <p class="website">www.TidewayTrips.example</p>
  </section>
</body>
</html>
```